Industrial CNC laser cutting machine manufacturer needs a website designed

We need a website design for our company that re manufactures CNC laser cutting machines, we take old retired machines and completely re manufacture them from the ground up bringing them into the latest technology with all new parts and give them a new lease on life for a fraction of the cost of a new machine.

Machines can be fully customized to suit customers requirements too

My logo will need to be integrated and I want the website to look clean and modern

I will probably want 4 pages,Home, pictures, machines for sale and contact

```html
<!DOCTYPE html>
<html lang="en">
<head>
<meta charset="utf-8">
<title>Beamline Rebuild Works – Home</title>
<link href="https://fonts.googleapis.com/css2?family=Rajdhani:wght@600;700&family=Roboto:wght@400;500;700&display=swap" rel="stylesheet">
<style>
:root{
  --red:#ec1c24;
  --dark:#4a4a4a;
  --ink:#1c1c1c;
  --grey:#7a7a7a;
  --muted:#8c8c8c;
  --stage:#bdbdbd;
  --field:#efefef;
  --white:#fff;
  --svc-light:#eeeeee;
  --svc-dark:#8b8b8d;
}
*{margin:0;padding:0;box-sizing:border-box}
html,body{width:768px;height:1200px;overflow:hidden;background:var(--stage)}
body{position:relative;font-family:"Roboto",sans-serif;color:var(--ink)}
.page{position:absolute;top:47px;width:330px;height:1108px;background:var(--white);overflow:hidden}
.page--a{left:37px}.page--b{left:403px}
.abs{position:absolute}
.heading{font-family:"Rajdhani",sans-serif;font-weight:700;text-transform:uppercase;line-height:1}
.heading .soft{color:var(--grey)}
.btn{position:absolute;background:var(--red);color:#fff;font-size:4px;font-weight:700;text-transform:uppercase;display:flex;align-items:center;justify-content:center;gap:2px}
.btn::after{content:"";width:3px;height:3px;border-radius:50%;background:#fff}
.dots{position:absolute;left:50%;transform:translateX(-50%);width:24px;height:3px}
/* header */
.site-header{top:0;left:0;width:330px;height:26px}
.brand{left:31px;top:10px;font-size:4.6px;font-weight:700;color:var(--grey);letter-spacing:.1px;display:flex;align-items:center;gap:3px;white-space:nowrap}
.brand i{width:5px;height:5px;background:var(--red);display:block}
.nav{left:120px;top:11px;display:flex;gap:5px;font-size:4px;white-space:nowrap}
.nav a{color:var(--ink);text-decoration:none}
.nav a.active{color:var(--red)}
.call{left:248px;top:7px}
.call small{display:block;font-size:3px;color:var(--grey);margin-left:10px}
.call b{font-size:5.5px;font-weight:700;display:flex;align-items:center;gap:3px;white-space:nowrap}
/* hero */
.hero{top:26px;left:0;width:330px;height:183px;background:radial-gradient(ellipse at 50% 55%,#e2a255 0%,#7a4a2a 25%,#2b2f44 60%,#171b2a 100%)}
.hero-box{left:75px;top:44px;width:180px;height:72px;background:rgba(40,40,50,.35)}
.hero-title{left:0;width:330px;top:49px;text-align:center;color:#fff;font-size:12px;white-space:nowrap}
.hero-text{left:85px;width:160px;top:68px;text-align:center;color:#fff;font-size:4px;line-height:1.8}
.arrow-c{width:9px;height:9px;border:.7px solid #fff;border-radius:50%;top:73px}
.hero-edge{left:0;bottom:0}
/* about */
.about-photo{left:31px;top:219px;width:102px;height:102px;border-radius:50%;background:linear-gradient(160deg,#d8d4cf 0%,#ee6a24 45%,#b8471a 80%,#6d6a66 100%)}
.about-inset{left:98px;top:283px;width:43px;height:43px;border-radius:50%;border:2px solid #fff;background:linear-gradient(150deg,#cfcac3,#c4512a 70%)}
.play{left:116px;top:302px;width:7px;height:7px;border-radius:50%;background:#fff}
.eyebrow{color:var(--red);font-size:4.5px;font-weight:700;text-transform:uppercase}
.about-copy{left:163px;top:222px;width:150px}
.about-copy h2{font-size:9.5px;margin-top:5px}
.about-copy p{font-size:3.4px;color:var(--grey);line-height:1.9;margin-top:6px}
/* services */
.services{top:350px;left:0;width:330px;height:158px;background:var(--svc-light)}
.page--b .services{background:var(--svc-dark)}
.services .heading{font-size:9.5px;width:330px;text-align:center;top:30px}
.services .eyebrow{width:330px;text-align:center;top:21px;font-size:4.5px}
.card{top:46px;width:86px;height:82px;background:#fff;border-radius:14px 0 14px 0;text-align:center;padding-top:7px}
.card .ico{width:26px;height:26px;border-radius:50%;background:#666;margin:0 auto}
.card h3{font-size:4.6px;font-weight:500;text-transform:uppercase;margin-top:6px}
.card p{font-size:3.4px;color:var(--grey);line-height:1.75;margin:3px 7px 0}
.card .more{font-size:3.6px;font-weight:700;color:#b2191f;margin-top:5px;text-transform:uppercase}
.card--hot{background:var(--red);color:#fff}
.card--hot .ico{background:#fff}
.card--hot p,.card--hot .more{color:#fff}
.card--muted .more{color:var(--grey)}
/* gallery */
.gallery-title{top:530px;width:330px;text-align:center;font-size:10px}
.shot{height:60px}
.shot--1{background:linear-gradient(135deg,#8c8a86,#e6e6e4 45%,#ec6b24 75%,#5a524a)}
.shot--2{background:linear-gradient(165deg,#c9c6c0,#9a968e 35%,#ee6a22 60%,#7d7a74)}
.shot--3{background:linear-gradient(120deg,#ef7428,#c9c9c9 40%,#e06624 70%,#555)}
.shot--4{background:linear-gradient(180deg,#e9e9e9,#8a8175 50%,#e8742b 80%,#4b4b4b)}
.shot--5{background:linear-gradient(150deg,#dcdad6,#ee6a24 45%,#7aa04a 55%,#5a5a5a)}
/* testimonial */
.testimonial{top:738px;left:0;width:330px;height:92px;background:var(--red);color:#fff}
.testimonial h2{left:88px;top:13px;font-size:9.5px;white-space:nowrap}
.avatar{left:51px;top:39px;width:26px;height:26px;transform:rotate(45deg);background:linear-gradient(135deg,#bfe3f5,#4a8cc0);border-radius:3px}
.quote{left:88px;top:38px;width:186px;font-size:3.9px;font-style:italic;line-height:1.9}
.quote-mark{font-family:Georgia,serif;font-size:11px;line-height:1;color:rgba(255,255,255,.45)}
.who{left:88px;top:64px;line-height:1.3}
.who b{font-size:4.6px;font-weight:500;display:block}
.who small{font-size:3.2px;display:block}
.chev{top:41px;width:6px;height:6px;border-left:1px solid #fff;border-bottom:1px solid #fff}
/* contact */
.contact-title{top:852px;width:330px;text-align:center;font-size:10px}
.col-title{font-size:5.5px;color:var(--grey);font-weight:500}
.detail{left:31px;display:flex;gap:8px;font-size:3.8px;color:var(--grey);line-height:1.75;width:110px}
.detail b{color:var(--ink);font-weight:500;font-size:4.2px}
.detail svg{flex:none}
.social{top:964px;left:31px;display:flex;gap:3px}
.social span{width:9px;height:9px;border-radius:50%;background:var(--red)}
.field{background:var(--field);border:.5px solid #e2e2e2;font-size:3px;color:var(--muted);padding:3px 5px}
/* footer */
.footer{top:995px;left:0;width:330px;height:113px;background:var(--dark);color:#fff}
.footer-edge{left:0;top:0}
.footer-brand{top:43px;width:330px;text-align:center;font-size:7px;font-weight:700;color:#9a9a9a}
.footer-nav{top:61px;width:330px;text-align:center;font-size:4.2px}
.footer-line{font-size:3.8px;display:flex;gap:6px;align-items:center;left:31px}
.ring{width:11px;height:11px;border:.7px solid #fff;border-radius:50%}
.legal{right:31px;font-size:3.6px;text-align:right;line-height:2.6;top:78px}
.redline{left:0;bottom:0;width:330px;height:1px;background:var(--red)}
</style>
</head>
<body>

<section class="page page--a">
  <header class="abs site-header">
    <div class="abs brand"><i></i>BEAMLINE REBUILD WORKS</div>
    <nav class="abs nav"><a class="active" href="#">Home</a><a href="#">Pictures</a><a href="#">Machines for sale</a><a href="#">About</a><a href="#">Contact</a></nav>
    <div class="abs call"><small>Call Us</small><b><svg width="7" height="7" viewBox="0 0 10 10"><path d="M2 1l2 2-1 1.5c.6 1.2 1.3 1.9 2.5 2.5L7 6l2 2-1.5 1.5C4.5 9 1 5.5.5 2.5z" fill="#ec1c24"/></svg>(555) 014-2290</b></div>
  </header>

  <div class="abs hero" role="img" aria-label="Laser cutting head throwing sparks onto sheet metal">
    <div class="abs hero-box"></div>
    <h1 class="abs heading hero-title">Beamline Rebuild Works</h1>
    <p class="abs hero-text">Lorem ipsum dolor sit amet, consectetur adipiscing elit, sed do eiusmod tempor incididunt</p>
    <a class="btn" style="left:140px;top:89px;width:49px;height:12px;font-size:4.4px">Get Started</a>
    <span class="abs arrow-c" style="left:10px"></span>
    <span class="abs arrow-c" style="left:311px"></span>
    <svg class="abs hero-edge" width="330" height="45" viewBox="0 0 330 45"><polygon points="110,25 330,4 330,45 150,45" fill="#ec1c24"/><polygon points="0,41 330,45 0,45" fill="#fff"/></svg>
  </div>

  <div class="abs about-photo" role="img" aria-label="Rebuilt orange laser cutting machine in workshop"></div>
  <div class="abs about-inset" role="img" aria-label="Video still of machine assembly"></div>
  <svg class="abs play" viewBox="0 0 10 10"><polygon points="4,3 7,5 4,7" fill="#555"/></svg>
  <div class="abs about-copy">
    <div class="eyebrow">About</div>
    <h2 class="heading">We take old retired machines<br><span class="soft">and re-manufacture</span></h2>
    <p>Sed ut perspiciatis unde omnis iste natus error sit voluptatem accusantium doloremque laudantium, totam rem aperiam, eaque ipsa quae ab illo inventore veritatis et quasi architecto beatae vitae dicta sunt explicabo. Nemo enim ipsam voluptatem quia</p>
    <p style="margin-top:3px">Sed ut perspiciatis unde omnis iste natus error sit voluptatem accusantium doloremque laudantium, totam rem aperiam,</p>
  </div>
  <a class="btn" style="left:163px;top:313px;width:55px;height:12px">Machines for sale</a>

  <section class="abs services">
    <div class="abs eyebrow">— We provide —</div>
    <h2 class="abs heading">Our <span class="soft">Services</span></h2>
    <article class="abs card" style="left:31px"><div class="ico"></div><h3>Services and Repair</h3><p>Lorem ipsum dolor sit amet, consectetur adipiscing elit, sed do eiusmod tempor incididunt ut labore et dolore</p><div class="more">Read more ›</div></article>
    <article class="abs card card--hot" style="left:122px"><div class="ico"></div><h3>Machines for Sale</h3><p>Lorem ipsum dolor sit amet, consectetur adipiscing elit, sed do eiusmod tempor incididunt ut labore et dolore</p><div class="more">Read more ›</div></article>
    <article class="abs card card--muted" style="left:213px"><div class="ico"></div><h3>Re-Manufacture</h3><p>Lorem ipsum dolor sit amet, consectetur adipiscing elit, sed do eiusmod tempor incididunt ut labore et dolore</p><div class="more">Read more ›</div></article>
  </section>

  <h2 class="abs heading gallery-title">Our <span class="soft">Gallery</span></h2>
  <svg class="dots" style="top:545px" viewBox="0 0 24 3"><line x1="0" y1="1.5" x2="8" y2="1.5" stroke="#ec1c24" stroke-width=".6"/><line x1="16" y1="1.5" x2="24" y2="1.5" stroke="#ec1c24" stroke-width=".6"/><circle cx="9.5" cy="1.5" r=".7" fill="#ec1c24"/><circle cx="12" cy="1.5" r="1.2" fill="#ec1c24"/><circle cx="14.5" cy="1.5" r=".7" fill="#ec1c24"/></svg>
  <div class="abs shot shot--1" style="left:31px;top:559px;width:131px" role="img" aria-label="Rebuilt laser machine with white enclosure"></div>
  <div class="abs shot shot--2" style="left:168px;top:559px;width:131px" role="img" aria-label="Orange cutting bed in workshop"></div>
  <div class="abs shot shot--3" style="left:31px;top:624px;width:85px" role="img" aria-label="Close view of machine gantry"></div>
  <div class="abs shot shot--4" style="left:122px;top:624px;width:85px" role="img" aria-label="Inside the machine cabin"></div>
  <div class="abs shot shot--5" style="left:213px;top:624px;width:86px" role="img" aria-label="Finished orange laser cutter"></div>
  <a class="btn" style="left:135px;top:696px;width:60px;height:13px">See all gallery</a>

  <section class="abs testimonial">
    <h2 class="abs heading">What our clients have to say</h2>
    <svg class="dots" style="top:26px" viewBox="0 0 24 3"><line x1="0" y1="1.5" x2="8" y2="1.5" stroke="#fff" stroke-width=".6"/><line x1="16" y1="1.5" x2="24" y2="1.5" stroke="#fff" stroke-width=".6"/><circle cx="9.5" cy="1.5" r=".7" fill="#fff"/><circle cx="12" cy="1.5" r="1.2" fill="#fff"/><circle cx="14.5" cy="1.5" r=".7" fill="#fff"/></svg>
    <span class="abs quote-mark" style="left:78px;top:30px">“</span>
    <div class="abs avatar" role="img" aria-label="Client portrait"></div>
    <p class="abs quote">Lorem ipsum dolor sit amet, consectetur adipiscing elit, sed do eiusmod tempor incididunt ut labore et dolore magna aliqua. Ut enim ad minim veniam, quis nostrud exercitation ullamco laboris nisi ut aliquip ex ea commodo consequat.</p>
    <span class="abs quote-mark" style="left:158px;top:55px">”</span>
    <div class="abs who"><b>Dana Reyes</b><small>Company Name</small></div>
    <span class="abs chev" style="left:32px;transform:rotate(45deg)"></span>
    <span class="abs chev" style="left:292px;transform:rotate(-135deg)"></span>
  </section>

  <h2 class="abs heading contact-title">Contact <span class="soft">Us</span></h2>
  <svg class="dots" style="top:867px" viewBox="0 0 24 3"><line x1="0" y1="1.5" x2="8" y2="1.5" stroke="#ec1c24" stroke-width=".6"/><line x1="16" y1="1.5" x2="24" y2="1.5" stroke="#ec1c24" stroke-width=".6"/><circle cx="9.5" cy="1.5" r=".7" fill="#ec1c24"/><circle cx="12" cy="1.5" r="1.2" fill="#ec1c24"/><circle cx="14.5" cy="1.5" r=".7" fill="#ec1c24"/></svg>
  <div class="abs col-title" style="left:31px;top:885px">Contact Details</div>
  <div class="abs col-title" style="left:154px;top:885px">Get In Touch</div>
  <div class="abs detail" style="top:900px"><svg width="8" height="10" viewBox="0 0 8 10"><path d="M4 0a4 4 0 0 1 4 4c0 3-4 6-4 6S0 7 0 4a4 4 0 0 1 4-4z" fill="#ec1c24"/><circle cx="4" cy="4" r="1.4" fill="#fff"/></svg><span>123, Lorem ipsum dolor sit amet, consectetur adipiscing elit, sed do</span></div>
  <div class="abs detail" style="top:921px"><svg width="9" height="9" viewBox="0 0 10 10"><path d="M2 1l2 2-1 1.5c.6 1.2 1.3 1.9 2.5 2.5L7 6l2 2-1.5 1.5C4.5 9 1 5.5.5 2.5z" fill="none" stroke="#ec1c24" stroke-width=".8"/></svg><span><b>PHONE NUMBER</b><br>555 014 2290</span></div>
  <div class="abs detail" style="top:942px"><svg width="9" height="7" viewBox="0 0 10 8"><rect x=".5" y=".5" width="9" height="7" fill="none" stroke="#ec1c24" stroke-width=".8"/><path d="M.5.5l4.5 4 4.5-4" fill="none" stroke="#ec1c24" stroke-width=".8"/></svg><span><b>EMAIL</b><br>info@beamlinerebuild.com</span></div>
  <div class="abs social"><span></span><span></span><span></span></div>
  <div class="abs field" style="left:154px;top:901px;width:68px;height:12px">Name</div>
  <div class="abs field" style="left:231px;top:901px;width:68px;height:12px">Phone Number</div>
  <div class="abs field" style="left:154px;top:917px;width:68px;height:12px">Email Address</div>
  <div class="abs field" style="left:231px;top:917px;width:68px;height:12px">Subject</div>
  <div class="abs field" style="left:154px;top:933px;width:145px;height:23px">Message</div>
  <a class="btn" style="left:154px;top:964px;width:32px;height:11px">Submit</a>

  <footer class="abs footer">
    <svg class="abs footer-edge" width="330" height="48" viewBox="0 0 330 48"><polygon points="0,0 330,0 0,48" fill="#fff"/><polygon points="0,0 165,25 0,48" fill="#ec1c24"/></svg>
    <div class="abs footer-brand">BEAMLINE REBUILD WORKS</div>
    <div class="abs footer-nav">Home &nbsp;/&nbsp; Pictures &nbsp;/&nbsp; Machines for Sale &nbsp;/&nbsp; About &nbsp;/&nbsp; Contact</div>
    <div class="abs footer-line" style="top:80px">☏&nbsp; 555 014 2290</div>
    <div class="abs footer-line" style="top:91px">✉&nbsp; info@beamlinerebuild.com</div>
    <div class="abs" style="left:137px;top:80px;display:flex;gap:4px"><span class="ring"></span><span class="ring"></span><span class="ring"></span><span class="ring"></span></div>
    <div class="abs legal">© Copyright 2020 Beamline Rebuild Works.<br>All Rights Reserved</div>
    <div class="abs redline"></div>
  </footer>
</section>

<section class="page page--b">
  <header class="abs site-header">
    <div class="abs brand"><i></i>BEAMLINE REBUILD WORKS</div>
    <nav class="abs nav"><a class="active" href="#">Home</a><a href="#">Pictures</a><a href="#">Machines for sale</a><a href="#">About</a><a href="#">Contact</a></nav>
    <div class="abs call"><small>Call Us</small><b><svg width="7" height="7" viewBox="0 0 10 10"><path d="M2 1l2 2-1 1.5c.6 1.2 1.3 1.9 2.5 2.5L7 6l2 2-1.5 1.5C4.5 9 1 5.5.5 2.5z" fill="#ec1c24"/></svg>(555) 014-2290</b></div>
  </header>

  <div class="abs hero" role="img" aria-label="Laser cutting head throwing sparks onto sheet metal">
    <div class="abs hero-box"></div>
    <h1 class="abs heading hero-title">Beamline Rebuild Works</h1>
    <p class="abs hero-text">Lorem ipsum dolor sit amet, consectetur adipiscing elit, sed do eiusmod tempor incididunt</p>
    <a class="btn" style="left:140px;top:89px;width:49px;height:12px;font-size:4.4px">Get Started</a>
    <span class="abs arrow-c" style="left:10px"></span>
    <span class="abs arrow-c" style="left:311px"></span>
    <svg class="abs hero-edge" width="330" height="45" viewBox="0 0 330 45"><polygon points="110,25 330,4 330,45 150,45" fill="#ec1c24"/><polygon points="0,41 330,45 0,45" fill="#fff"/></svg>
  </div>

  <div class="abs about-photo" role="img" aria-label="Rebuilt orange laser cutting machine in workshop"></div>
  <div class="abs about-inset" role="img" aria-label="Video still of machine assembly"></div>
  <svg class="abs play" viewBox="0 0 10 10"><polygon points="4,3 7,5 4,7" fill="#555"/></svg>
  <div class="abs about-copy">
    <div class="eyebrow">About</div>
    <h2 class="heading">We take old retired machines<br><span class="soft">and re-manufacture</span></h2>
    <p>Sed ut perspiciatis unde omnis iste natus error sit voluptatem accusantium doloremque laudantium, totam rem aperiam, eaque ipsa quae ab illo inventore veritatis et quasi architecto beatae vitae dicta sunt explicabo. Nemo enim ipsam voluptatem quia</p>
    <p style="margin-top:3px">Sed ut perspiciatis unde omnis iste natus error sit voluptatem accusantium doloremque laudantium, totam rem aperiam,</p>
  </div>
  <a class="btn" style="left:163px;top:313px;width:55px;height:12px">Machines for sale</a>

  <section class="abs services">
    <div class="abs eyebrow">— We provide —</div>
    <h2 class="abs heading" style="color:#fff">Our <span class="soft" style="color:#e6e6e6">Services</span></h2>
    <article class="abs card" style="left:31px"><div class="ico"></div><h3>Services and Repair</h3><p>Lorem ipsum dolor sit amet, consectetur adipiscing elit, sed do eiusmod tempor incididunt ut labore et dolore</p><div class="more">Read more ›</div></article>
    <article class="abs card card--hot" style="left:122px"><div class="ico"></div><h3>Machines for Sale</h3><p>Lorem ipsum dolor sit amet, consectetur adipiscing elit, sed do eiusmod tempor incididunt ut labore et dolore</p><div class="more">Read more ›</div></article>
    <article class="abs card card--muted" style="left:213px"><div class="ico"></div><h3>Re-Manufacture</h3><p>Lorem ipsum dolor sit amet, consectetur adipiscing elit, sed do eiusmod tempor incididunt ut labore et dolore</p><div class="more">Read more ›</div></article>
  </section>

  <h2 class="abs heading gallery-title">Our <span class="soft">Gallery</span></h2>
  <svg class="dots" style="top:545px" viewBox="0 0 24 3"><line x1="0" y1="1.5" x2="8" y2="1.5" stroke="#ec1c24" stroke-width=".6"/><line x1="16" y1="1.5" x2="24" y2="1.5" stroke="#ec1c24" stroke-width=".6"/><circle cx="9.5" cy="1.5" r=".7" fill="#ec1c24"/><circle cx="12" cy="1.5" r="1.2" fill="#ec1c24"/><circle cx="14.5" cy="1.5" r=".7" fill="#ec1c24"/></svg>
  <div class="abs shot shot--1" style="left:31px;top:559px;width:131px" role="img" aria-label="Rebuilt laser machine with white enclosure"></div>
  <div class="abs shot shot--2" style="left:168px;top:559px;width:131px" role="img" aria-label="Orange cutting bed in workshop"></div>
  <div class="abs shot shot--3" style="left:31px;top:624px;width:85px" role="img" aria-label="Close view of machine gantry"></div>
  <div class="abs shot shot--4" style="left:122px;top:624px;width:85px" role="img" aria-label="Inside the machine cabin"></div>
  <div class="abs shot shot--5" style="left:213px;top:624px;width:86px" role="img" aria-label="Finished orange laser cutter"></div>
  <a class="btn" style="left:135px;top:696px;width:60px;height:13px">See all gallery</a>

  <section class="abs testimonial">
    <h2 class="abs heading">What our clients have to say</h2>
    <svg class="dots" style="top:26px" viewBox="0 0 24 3"><line x1="0" y1="1.5" x2="8" y2="1.5" stroke="#fff" stroke-width=".6"/><line x1="16" y1="1.5" x2="24" y2="1.5" stroke="#fff" stroke-width=".6"/><circle cx="9.5" cy="1.5" r=".7" fill="#fff"/><circle cx="12" cy="1.5" r="1.2" fill="#fff"/><circle cx="14.5" cy="1.5" r=".7" fill="#fff"/></svg>
    <span class="abs quote-mark" style="left:78px;top:30px">“</span>
    <div class="abs avatar" role="img" aria-label="Client portrait"></div>
    <p class="abs quote">Lorem ipsum dolor sit amet, consectetur adipiscing elit, sed do eiusmod tempor incididunt ut labore et dolore magna aliqua. Ut enim ad minim veniam, quis nostrud exercitation ullamco laboris nisi ut aliquip ex ea commodo consequat.</p>
    <span class="abs quote-mark" style="left:158px;top:55px">”</span>
    <div class="abs who"><b>Dana Reyes</b><small>Company Name</small></div>
    <span class="abs chev" style="left:32px;transform:rotate(45deg)"></span>
    <span class="abs chev" style="left:292px;transform:rotate(-135deg)"></span>
  </section>

  <h2 class="abs heading contact-title">Contact <span class="soft">Us</span></h2>
  <svg class="dots" style="top:867px" viewBox="0 0 24 3"><line x1="0" y1="1.5" x2="8" y2="1.5" stroke="#ec1c24" stroke-width=".6"/><line x1="16" y1="1.5" x2="24" y2="1.5" stroke="#ec1c24" stroke-width=".6"/><circle cx="9.5" cy="1.5" r=".7" fill="#ec1c24"/><circle cx="12" cy="1.5" r="1.2" fill="#ec1c24"/><circle cx="14.5" cy="1.5" r=".7" fill="#ec1c24"/></svg>
  <div class="abs col-title" style="left:31px;top:885px">Contact Details</div>
  <div class="abs col-title" style="left:154px;top:885px">Get In Touch</div>
  <div class="abs detail" style="top:900px"><svg width="8" height="10" viewBox="0 0 8 10"><path d="M4 0a4 4 0 0 1 4 4c0 3-4 6-4 6S0 7 0 4a4 4 0 0 1 4-4z" fill="#ec1c24"/><circle cx="4" cy="4" r="1.4" fill="#fff"/></svg><span>123, Lorem ipsum dolor sit amet, consectetur adipiscing elit, sed do</span></div>
  <div class="abs detail" style="top:921px"><svg width="9" height="9" viewBox="0 0 10 10"><path d="M2 1l2 2-1 1.5c.6 1.2 1.3 1.9 2.5 2.5L7 6l2 2-1.5 1.5C4.5 9 1 5.5.5 2.5z" fill="none" stroke="#ec1c24" stroke-width=".8"/></svg><span><b>PHONE NUMBER</b><br>555 014 2290</span></div>
  <div class="abs detail" style="top:942px"><svg width="9" height="7" viewBox="0 0 10 8"><rect x=".5" y=".5" width="9" height="7" fill="none" stroke="#ec1c24" stroke-width=".8"/><path d="M.5.5l4.5 4 4.5-4" fill="none" stroke="#ec1c24" stroke-width=".8"/></svg><span><b>EMAIL</b><br>info@beamlinerebuild.com</span></div>
  <div class="abs social"><span></span><span></span><span></span></div>
  <div class="abs field" style="left:154px;top:901px;width:68px;height:12px">Name</div>
  <div class="abs field" style="left:231px;top:901px;width:68px;height:12px">Phone Number</div>
  <div class="abs field" style="left:154px;top:917px;width:68px;height:12px">Email Address</div>
  <div class="abs field" style="left:231px;top:917px;width:68px;height:12px">Subject</div>
  <div class="abs field" style="left:154px;top:933px;width:145px;height:23px">Message</div>
  <a class="btn" style="left:154px;top:964px;width:32px;height:11px">Submit</a>

  <footer class="abs footer">
    <svg class="abs footer-edge" width="330" height="48" viewBox="0 0 330 48"><polygon points="0,0 330,0 0,48" fill="#fff"/><polygon points="0,0 165,25 0,48" fill="#ec1c24"/></svg>
    <div class="abs footer-brand">BEAMLINE REBUILD WORKS</div>
    <div class="abs footer-nav">Home &nbsp;/&nbsp; Pictures &nbsp;/&nbsp; Machines for Sale &nbsp;/&nbsp; About &nbsp;/&nbsp; Contact</div>
    <div class="abs footer-line" style="top:80px">☏&nbsp; 555 014 2290</div>
    <div class="abs footer-line" style="top:91px">✉&nbsp; info@beamlinerebuild.com</div>
    <div class="abs" style="left:137px;top:80px;display:flex;gap:4px"><span class="ring"></span><span class="ring"></span><span class="ring"></span><span class="ring"></span></div>
    <div class="abs legal">© Copyright 2020 Beamline Rebuild Works.<br>All Rights Reserved</div>
    <div class="abs redline"></div>
  </footer>
</section>

</body>
</html>
```